Task Scheduling Web App

I have a basic web app that I need designed. It must be mobile-first but it needs to be responsive for desktop users as well.
1. Before beginning the exercise, the user inputs basic info on their country and age.
2. The user is then presented with two piles of cards (TASK or DAY), with the top card face up. They have 20 seconds before their combination is set, during which they can replace either of the cards at random as many times as they like. At any time they find a combination they’re happy with, they can progress to the next screen. If the clock runs out the combination is set based on whatever cards are showing at the time and they’re moved on to the next screen.
3. The user is presented with a blank graph; x axis is ‘How important is it?’, y axis is ‘How often does it need to be done?’. The two cards they picked in the previous screen are combined to create a COMBO and the user must place a mark somewhere on the graph to represent how important they believe the scheduled task to be vs how often it will need to be done.
4. Once the user has picked a spot on the graph, options appear for them to re-do the exercise by choosing a new combo or to progress and see how their peers are organising their tasks.
5. If they choose to view insights, they must login with Villowry so a popup will appear to facilitate this.
6. After logging in with Villowry, users can view the top 10 combinations for their demographic listed and mapped on a graph. This information is based on the selection and ranking of combinations by other users.

```html
<!DOCTYPE html>
<html lang="en">
<head>
<meta charset="utf-8">
<title>Task Scheduling — User Information</title>
<link href="https://fonts.googleapis.com/css2?family=Ubuntu:wght@400;500;700&display=swap" rel="stylesheet">
<style>
  :root{
    --page-bg:#f1f1ef;
    --status-bg:#2c2c2c;
    --status-text:#f2f2f2;
    --nav-green:#7fd39a;
    --nav-green-dark:#5fb97c;
    --btn-green:#6cc68a;
    --btn-green-edge:#4aa86a;
    --card-bg:#f4f0e6;
    --ink:#2a2a2a;
    --ink-soft:#4a4a4a;
    --accent-coral:#ee7a63;
    --field-bg:#ffffff;
    --track:#dedbd2;
  }
  *{box-sizing:border-box;margin:0;padding:0}
  html,body{width:1014px;height:1200px;overflow:hidden;background:var(--page-bg)}
  body{font-family:"Ubuntu",sans-serif;position:relative}
  .app-screen{
    position:absolute;left:169px;top:0;width:676px;height:1200px;overflow:hidden;
    background:
      radial-gradient(ellipse at 15% 60%, rgba(230,205,160,.55), transparent 55%),
      radial-gradient(ellipse at 80% 95%, rgba(235,190,160,.7), transparent 55%),
      linear-gradient(180deg,#efe4cf 0%,#efdcc3 30%,#e8d8c2 65%,#e8c9b0 100%);
  }
  .status-bar{
    height:39px;background:var(--status-bg);color:var(--status-text);
    display:flex;align-items:center;justify-content:space-between;padding:0 12px;
    font-weight:700;font-size:25px;
  }
  .status-bar .time{position:absolute;left:0;right:0;text-align:center;pointer-events:none}
  .nav-bar{
    position:relative;height:100px;background:linear-gradient(180deg,#8cdca6,var(--nav-green));
    border-bottom:2px solid var(--nav-green-dark);
    display:flex;align-items:center;justify-content:space-between;padding:0 14px 0 17px;
  }
  .back-button{
    height:64px;width:110px;border:2px solid var(--nav-green-dark);border-radius:6px 8px 8px 6px;
    background:var(--btn-green);color:#fff;font-weight:500;font-size:28px;
    display:flex;align-items:center;justify-content:center;padding-left:8px;
  }
  .app-title{
    position:absolute;left:0;right:0;text-align:center;color:#fff;font-weight:500;font-size:44px;
    pointer-events:none;
  }
  .settings-button{
    width:60px;height:60px;border:2px solid var(--nav-green-dark);border-radius:6px;
    background:var(--btn-green);display:flex;align-items:center;justify-content:center;
  }
  .form-card{
    position:absolute;left:56px;top:309px;width:561px;height:776px;background:var(--card-bg);
    box-shadow:0 0 3px rgba(0,0,0,.08);
  }
  .step-label{position:absolute;left:62px;top:22px;font-size:18px;font-weight:500;color:var(--ink-soft)}
  .progress{position:absolute;left:38px;top:75px;width:470px;height:16px;border-radius:8px;background:var(--track);box-shadow:inset 0 1px 2px rgba(0,0,0,.15)}
  .progress-fill{position:absolute;left:0;top:0;height:16px;width:86px;border-radius:8px;background:var(--btn-green)}
  .progress-knob{position:absolute;left:60px;top:-17px;width:50px;height:50px;border-radius:50%;
    background:radial-gradient(circle at 45% 40%,#fdfdfd,#cfcfcf 60%,#a9a9a9);box-shadow:0 2px 4px rgba(0,0,0,.3)}
  .section-title{position:absolute;left:0;right:0;top:150px;text-align:center;font-size:46px;font-weight:500;letter-spacing:1px;color:var(--ink)}
  .section-intro{position:absolute;left:0;right:0;top:212px;text-align:center;font-size:18px;line-height:23px;color:var(--ink-soft)}
  .select-field{
    position:absolute;left:41px;width:473px;height:64px;background:var(--field-bg);
    display:flex;align-items:center;justify-content:space-between;padding:0 22px;
    color:var(--accent-coral);font-size:23px;font-weight:500;
  }
  .field-country{top:300px}
  .field-age{top:391px}
  .go-button{
    position:absolute;left:39px;top:528px;width:477px;height:72px;border-radius:6px;
    background:linear-gradient(180deg,#8fdcaa,var(--btn-green));border:2px solid var(--btn-green-edge);
    box-shadow:0 5px 0 #4f9e6b;color:#fff;font-size:38px;font-weight:700;
    display:flex;align-items:center;justify-content:center;
  }
</style>
</head>
<body>
  <main class="app-screen">
    <div class="status-bar">
      <svg width="44" height="22" viewBox="0 0 44 22" aria-label="Signal strength">
        <rect x="2" y="17" width="5" height="4" fill="#f2f2f2"/><rect x="10" y="14" width="5" height="7" fill="#f2f2f2"/>
        <rect x="18" y="10" width="5" height="11" fill="#f2f2f2"/><rect x="26" y="5" width="5" height="16" fill="#f2f2f2"/>
        <rect x="34" y="1" width="5" height="20" fill="#f2f2f2"/>
      </svg>
      <span class="time">4:20 PM</span>
      <svg width="46" height="22" viewBox="0 0 46 22" aria-label="Battery">
        <rect x="1" y="2" width="38" height="18" rx="3" fill="none" stroke="#f2f2f2" stroke-width="2"/>
        <rect x="40" y="7" width="4" height="8" fill="#f2f2f2"/>
        <rect x="5" y="6" width="14" height="10" fill="#f2f2f2"/>
      </svg>
    </div>

    <header class="nav-bar">
      <div class="back-button">Back</div>
      <div class="app-title">Your App</div>
      <div class="settings-button">
        <svg width="32" height="32" viewBox="0 0 32 32" aria-label="Settings">
          <g fill="#fff">
            <circle cx="16" cy="16" r="10"/>
            <rect x="13" y="1" width="6" height="8" rx="1"/><rect x="13" y="23" width="6" height="8" rx="1"/>
            <rect x="1" y="13" width="8" height="6" rx="1"/><rect x="23" y="13" width="8" height="6" rx="1"/>
            <rect x="13" y="1" width="6" height="8" rx="1" transform="rotate(45 16 16)"/>
            <rect x="13" y="23" width="6" height="8" rx="1" transform="rotate(45 16 16)"/>
            <rect x="1" y="13" width="8" height="6" rx="1" transform="rotate(45 16 16)"/>
            <rect x="23" y="13" width="8" height="6" rx="1" transform="rotate(45 16 16)"/>
          </g>
          <circle cx="16" cy="16" r="4.5" fill="var(--btn-green)"/>
        </svg>
      </div>
    </header>

    <section class="form-card">
      <div class="step-label">STEP 1 OF 6</div>
      <div class="progress"><div class="progress-fill"></div><div class="progress-knob"></div></div>
      <h1 class="section-title">USER INFORMATION</h1>
      <p class="section-intro">To start the task scheduling exercise,<br>complete the following below:</p>

      <div class="select-field field-country">
        <span>Country</span>
        <svg width="18" height="12" viewBox="0 0 18 12"><path d="M2 2l7 7 7-7" fill="none" stroke="var(--accent-coral)" stroke-width="3.5"/></svg>
      </div>
      <div class="select-field field-age">
        <span>Age Range</span>
        <svg width="18" height="12" viewBox="0 0 18 12"><path d="M2 2l7 7 7-7" fill="none" stroke="var(--accent-coral)" stroke-width="3.5"/></svg>
      </div>

      <div class="go-button">GO</div>
    </section>
  </main>
</body>
</html>
```